Loom Haven needs a website

I sell rugs and carpet on my website, loomhavenfloors.example. I need help with the site design to make it "pop". The logo in the header has been designed and I want the site to match it's style and color. Also I have some example sites for layout:
matvale.example
weave-outlet.example

Industry/Entity Type

Carpet

Requirements
Must have
• Scrolling images on front page. I will insert photos, just need the code.

```html
<!DOCTYPE html>
<html lang="en">
<head>
<meta charset="utf-8">
<title>Loom Haven — Rugs &amp; Carpet</title>
<link href="https://fonts.googleapis.com/css2?family=Open+Sans:wght@400;600;700;800&display=swap" rel="stylesheet">
<style>
:root{
  --navy:#153f66;
  --navy-dark:#0f3252;
  --green:#76b767;
  --green-dark:#5ea24f;
  --green-light:#a3d194;
  --lime:#8cc63f;
  --page:#efefef;
  --text:#555;
  --white:#fff;
  --strip:#eef1f5;
  --red:#c0272d;
  --grey-badge:#9aa3ad;
}
*{margin:0;padding:0;box-sizing:border-box}
html,body{width:691px;height:1200px;overflow:hidden}
body{position:relative;background:var(--page);font-family:"Open Sans",Arial,sans-serif;color:var(--text)}
.abs{position:absolute}
a{color:inherit;text-decoration:none}
svg{display:block}

/* header */
.site-header{left:0;top:0;width:691px;height:70px;background:linear-gradient(#fff,#f1f3f1)}
.top-links{top:14px;display:flex;gap:14px;font-size:7px;color:#444}
.top-links span{display:flex;align-items:center;gap:4px}
.search{left:100px;top:36px;width:146px;height:17px;border:1px solid var(--green);background:#fff;font-size:6px;color:#999;padding:4px 5px}
.search svg{position:absolute;right:3px;top:3px}
.brand-tab{left:262px;top:0;width:166px;height:70px}
.brand{left:265px;top:0;width:160px;height:70px;display:flex;flex-direction:column;align-items:center;justify-content:center;gap:4px}
.brand-dot{width:30px;height:30px;border-radius:50%;background:var(--navy)}
.brand-name{font-size:17px;font-weight:600;color:var(--navy);line-height:1}
.cart{left:525px;top:36px;font-size:7px;color:#333;display:flex;align-items:center;gap:5px}

/* nav */
.main-nav{left:0;top:70px;width:691px;height:22px;background:linear-gradient(#8ccb7c,#6aad5b);display:flex;justify-content:center}
.main-nav ul{list-style:none;display:flex}
.main-nav li{font-size:8px;color:#fff;width:72px;text-align:center;line-height:22px;border-left:1px solid rgba(255,255,255,.35)}
.main-nav li:first-child{border-left:none}

/* hero */
.hero{left:0;top:92px;width:691px;height:223px;background:linear-gradient(100deg,#8a6a4a 0%,#a08466 18%,#6b5a4a 30%,#b9502f 45%,#c42a1e 52%,#7a3a3a 62%,#5c3f48 72%,#8a7a6c 85%,#a89a88 100%)}
.hero-caption{left:0;top:145px;width:290px;height:117px;background:rgba(40,30,25,.72);color:#fff;text-align:right;padding:3px 10px 0 0}
.hero-caption h1{font-weight:400;font-size:24px;line-height:28px}
.hero-caption h1 b{display:block;font-weight:800;font-size:29px;line-height:30px}
.hero-caption p{font-size:7px;line-height:10px;margin-top:5px;padding-left:110px}
.hero-arrow{width:16px;height:16px;border-radius:50%;background:rgba(255,255,255,.75);top:195px}
.hero-dots{left:254px;top:252px;display:flex;gap:3px}
.hero-dots i{width:6px;height:6px;border-radius:50%;background:#fff}
.hero-dots i:first-child{background:var(--green)}

/* offers */
.offer{top:289px;height:102px;color:#fff;overflow:hidden}
.offer h2{position:absolute;left:12px;top:8px;font-size:16px;font-weight:700}
.offer p{position:absolute;font-size:6.5px;line-height:9.5px}
.offer-special{left:99px;width:292px;background:var(--green)}
.offer-rugs{left:391px;width:201px;background:var(--green-light)}
.ribbon{right:-28px;top:12px;width:120px;height:20px;background:var(--navy);transform:rotate(40deg);font-size:11px;font-weight:800;color:#fff;text-align:center;line-height:20px}
.thumb{border:1px solid rgba(255,255,255,.6)}
.btn{background:var(--navy);color:#fff;font-size:6.5px;font-weight:700;border-radius:2px;display:flex;align-items:center;justify-content:center;gap:4px;height:16px;width:52px}
.btn i{width:8px;height:8px;border-radius:50%;background:#fff;display:flex;align-items:center;justify-content:center}

/* welcome */
.welcome{left:99px;top:410px;width:493px;text-align:center}
.welcome h2{font-size:17px;font-weight:400;color:var(--navy)}
.welcome p{font-size:6.5px;line-height:10px;color:#555;margin-top:8px;padding:0 12px}

/* categories */
.panel-head{background:var(--navy);color:#fff;font-size:8.5px;font-weight:700;height:22px;line-height:22px;padding:0 8px}
.categories{left:99px;top:540px;width:113px}
.cat-list{background:var(--green);height:183px;list-style:none;padding:6px 5px}
.cat-list li{font-size:6.5px;color:#fff;line-height:14.5px}
.cat-list li::before{content:"›";margin-right:4px}
.promo{left:99px;top:718px;width:113px;height:133px;background:#fff;padding:5px}
.promo-art{width:100%;height:100%;background:linear-gradient(135deg,#dfe7ea,#9fc7c9 55%,#4f6f72);position:relative}
.promo-text{position:absolute;left:4px;bottom:10px;color:#fff;background:rgba(40,40,40,.65);padding:2px 4px;font-weight:800;font-size:9px;line-height:10px}
.promo-text small{display:block;font-weight:600;font-size:5.5px;line-height:7px}

/* products */
.featured{left:232px;top:540px;width:360px}
.featured .panel-head{display:flex;justify-content:space-between;font-size:8px}
.product{width:107px;height:129px;background:#fff}
.product .img{height:75px}
.product p{font-size:6.5px;line-height:8.5px;color:#777;padding:6px 7px 0}
.price{position:absolute;left:7px;bottom:12px;display:flex;align-items:center;gap:3px;width:96px}
.price s{font-size:6.5px;color:#999}
.price b{font-size:9.5px;font-weight:400;color:var(--navy)}
.add{margin-left:auto;background:var(--lime);color:#fff;font-size:5.5px;font-weight:700;padding:3px 4px;border-radius:2px}
.img-a{background:linear-gradient(135deg,#7a4a22,#c99b62 50%,#5c3216)}
.img-b{background:linear-gradient(135deg,#2a2038,#6b5443 50%,#3b2e2a)}
.img-c{background:linear-gradient(135deg,#8a2a1c,#c8624a 50%,#6a2418)}

/* help */
.help{left:0;top:880px;width:691px;height:140px;background:linear-gradient(120deg,#e4e8ee,#d8dee6)}
.help h2{position:absolute;left:0;width:691px;top:20px;text-align:center;font-size:14px;font-weight:700;color:var(--navy)}
.help-line{top:29px;height:1px;background:#c9ced5;width:110px}
.help-item{top:55px;width:90px;text-align:center;font-size:7px;font-weight:700;color:#333}
.help-item .circle{width:54px;height:54px;border-radius:50%;background:var(--navy);margin:0 auto 12px;display:flex;align-items:center;justify-content:center}

/* partners */
.partners{left:0;top:1020px;width:691px;height:68px;background:var(--strip)}
.badge{top:27px;height:14px;background:var(--grey-badge);border-radius:2px}

/* footer */
.site-footer{left:0;top:1088px;width:691px;height:112px;background:var(--green)}
.foot-col{top:14px;color:#fff}
.foot-col h3{font-size:9px;font-weight:700;color:var(--navy);margin-bottom:6px}
.foot-col ul{list-style:none}
.foot-col li{font-size:6.5px;line-height:10.5px}
.foot-col li::before{content:"•";margin-right:4px}
.foot-col .small{font-size:6px}
.foot-brand{left:100px;top:1130px;width:124px;height:40px;background:rgba(255,255,255,.85);display:flex;align-items:center;justify-content:center;gap:5px}
.foot-brand .brand-dot{width:18px;height:18px}
.foot-brand .brand-name{font-size:13px}
.social{top:1177px;width:8px;height:8px;border-radius:50%;background:#fff}
</style>
</head>
<body>

<header class="site-header abs">
  <nav class="top-links abs" style="left:100px">
    <span><svg width="7" height="7" viewBox="0 0 10 10"><circle cx="5" cy="3" r="2.5" fill="#6a9f5d"/><path d="M0 10a5 4 0 0 1 10 0z" fill="#6a9f5d"/></svg>My Account</span>
    <span><svg width="7" height="7" viewBox="0 0 10 10"><path d="M5 9L1 5a2.3 2.3 0 0 1 4-3 2.3 2.3 0 0 1 4 3z" fill="#6a9f5d"/></svg>My Wishlist</span>
    <span><svg width="7" height="7" viewBox="0 0 10 10"><path d="M1 9V3h5M4 6l5-5M6 1h3v3" stroke="#6a9f5d" fill="none" stroke-width="1.4"/></svg>Checkout</span>
  </nav>
  <div class="search abs">Search
    <svg width="10" height="10" viewBox="0 0 10 10"><circle cx="4" cy="4" r="3" stroke="#153f66" stroke-width="1.6" fill="none"/><path d="M6.3 6.3L9.5 9.5" stroke="#153f66" stroke-width="1.8"/></svg>
  </div>
  <svg class="brand-tab abs" viewBox="0 0 166 70"><path d="M14 0h138l-10 70H24z" fill="#f4f6f4" stroke="#d7dcd7"/></svg>
  <a class="brand abs" href="#"><span class="brand-dot"></span><span class="brand-name">Loom Haven</span></a>
  <nav class="top-links abs" style="left:507px">
    <span><svg width="7" height="7" viewBox="0 0 10 10"><path d="M1 5h6M5 2l3 3-3 3" stroke="#6a9f5d" fill="none" stroke-width="1.5"/></svg>Log In</span>
    <span><svg width="7" height="7" viewBox="0 0 10 10"><path d="M1 1h5l3 4-4 4-4-3z" fill="#6a9f5d"/></svg>Register</span>
  </nav>
  <div class="cart abs"><svg width="11" height="10" viewBox="0 0 11 10"><path d="M0 1h2l2 6h6l1-4H3" stroke="#153f66" fill="#153f66" stroke-width="1"/><circle cx="5" cy="9" r="1" fill="#153f66"/><circle cx="9" cy="9" r="1" fill="#153f66"/></svg>0 item(s) - $0.00</div>
</header>

<nav class="main-nav abs">
  <ul><li>Home</li><li>About Us</li><li>Services</li><li>Gallery</li><li>Blog</li><li>Contact Us</li></ul>
</nav>

<section class="hero abs" role="img" aria-label="Slideshow photo: rows of carpet samples in beige, red and brown tones"></section>
<div class="hero-caption abs">
  <h1>Do not miss the<b>BIG ONE!</b></h1>
  <p>Sed vitae tincidunt dolor, et semper sapien. Duis hendrerit vitae elit quis commodo. Morbi eget purus sodales nibh volutpat mattis in id risus. In sed sodales dui.</p>
</div>
<div class="hero-arrow abs" style="left:21px"><svg width="16" height="16" viewBox="0 0 16 16"><path d="M9 5L6 8l3 3" stroke="#555" fill="none" stroke-width="1.4"/></svg></div>
<div class="hero-arrow abs" style="left:655px"><svg width="16" height="16" viewBox="0 0 16 16"><path d="M7 5l3 3-3 3" stroke="#555" fill="none" stroke-width="1.4"/></svg></div>
<div class="hero-dots abs"><i></i><i></i><i></i></div>

<section class="offer offer-special abs">
  <h2>Special Offer</h2>
  <div class="thumb abs" style="left:15px;top:32px;width:84px;height:50px;background:linear-gradient(90deg,#8a5a30,#c09060,#6a3a2a,#b08a50,#7a4a3a)" role="img" aria-label="Rolled rugs photo"></div>
  <p style="left:106px;top:35px;width:156px">Sed vitae tincidunt dolor, et semper sapien. Duis hendrerit vitae elit quis commodo. Morbi eget purus sodales nibh volutpat mattis in id risus. In sed sodales dui.</p>
  <div class="ribbon abs">30% Off</div>
  <a class="btn abs" style="left:205px;top:74px" href="#">View more <i><svg width="6" height="6" viewBox="0 0 6 6"><path d="M1 3h3M3 1.5L4.5 3 3 4.5" stroke="#153f66" fill="none"/></svg></i></a>
</section>
<section class="offer offer-rugs abs">
  <h2>Area Rugs</h2>
  <p style="left:13px;top:35px;width:88px">Sed vitae tincidunt dolor, et semper sapien. Duis hendr erit vitae elit quis comm</p>
  <div class="thumb abs" style="left:104px;top:31px;width:83px;height:50px;background:linear-gradient(135deg,#3a6f9a,#9ab5c8 50%,#6a7d88)" role="img" aria-label="Area rug corners photo"></div>
  <a class="btn abs" style="left:13px;top:74px" href="#">View more <i><svg width="6" height="6" viewBox="0 0 6 6"><path d="M1 3h3M3 1.5L4.5 3 3 4.5" stroke="#153f66" fill="none"/></svg></i></a>
</section>

<section class="welcome abs">
  <h2>Welcome to Loom Haven</h2>
  <p>Sed vitae tincidunt dolor, et semper sapien. Duis hendrerit vitae elit quis commodo. Morbi eget purus sodales nibh volutpat mattis in id risus. In sed sodales dui.</p>
  <p>Curabitur scelerisque vehicula orci. Nullam bibendum orci at sem commodo, nec pulvinar eros mollis. Aenean blandit dapibus elit ut sollicitudin. Suspendisse potenti. Vestibulum consequat nec elit vel bibendum. Donec eu volutpat massa, id faucibus dui. Proin luctus pulvinar nulla.</p>
</section>
<a class="btn abs" style="left:319px;top:500px" href="#">View more <i><svg width="6" height="6" viewBox="0 0 6 6"><path d="M1 3h3M3 1.5L4.5 3 3 4.5" stroke="#153f66" fill="none"/></svg></i></a>

<aside class="categories abs">
  <div class="panel-head">CATEGORIES</div>
  <ul class="cat-list">
    <li>Commercial Flooring</li><li>Carpet Flooring</li><li>Harwood Flooring</li><li>Area Rugs</li>
    <li>Vestibulum consequat nec</li><li>Elit vel bibendum. Donec eu</li><li>Volutpat massa, id faucibus</li>
    <li>Proin luctus pulvinar nulla.</li><li>Sed sit amet mollis sapien.</li><li>Vestibulum ante ipsum</li>
  </ul>
</aside>
<div class="promo abs">
  <div class="promo-art" role="img" aria-label="Accent pillows on a sofa">
    <div class="promo-text">10% OFF ACCENT PILLOWS<small>With purchase of any area rug.</small></div>
  </div>
</div>

<section class="featured abs">
  <div class="panel-head"><span>FEATURED PRODUCTS</span><span>View all »</span></div>
</section>

<article class="product abs" style="left:232px;top:577px"><div class="img img-a" role="img" aria-label="Checkered brown shag rug"></div><p>Aliquam et sem non turpis consequat varius in vel felis...</p><div class="price"><s>$92.50</s><b>$80.50</b><span class="add">Add to Cart</span></div></article>
<article class="product abs" style="left:359px;top:577px"><div class="img img-b" role="img" aria-label="Dark patterned oriental rug"></div><p>Aliquam et sem non turpis consequat varius in vel felis...</p><div class="price"><s>$92.50</s><b>$80.50</b><span class="add">Add to Cart</span></div></article>
<article class="product abs" style="left:486px;top:577px"><div class="img img-c" role="img" aria-label="Red floral oriental rug"></div><p>Aliquam et sem non turpis consequat varius in vel felis...</p><div class="price"><s>$92.50</s><b>$80.50</b><span class="add">Add to Cart</span></div></article>
<article class="product abs" style="left:232px;top:721px"><div class="img img-a" role="img" aria-label="Checkered brown shag rug"></div><p>Aliquam et sem non turpis consequat varius in vel felis...</p><div class="price"><s>$92.50</s><b>$80.50</b><span class="add">Add to Cart</span></div></article>
<article class="product abs" style="left:359px;top:721px"><div class="img img-b" role="img" aria-label="Dark patterned oriental rug"></div><p>Aliquam et sem non turpis consequat varius in vel felis...</p><div class="price"><s>$92.50</s><b>$80.50</b><span class="add">Add to Cart</span></div></article>
<article class="product abs" style="left:486px;top:721px"><div class="img img-c" role="img" aria-label="Red floral oriental rug"></div><p>Aliquam et sem non turpis consequat varius in vel felis...</p><div class="price"><s>$92.50</s><b>$80.50</b><span class="add">Add to Cart</span></div></article>

<section class="help abs" aria-label="Support">
  <div class="help-line abs" style="left:99px"></div>
  <h2>JUST IN CASE YOU NEED ANY HELP</h2>
  <div class="help-line abs" style="left:482px"></div>
  <div class="help-item abs" style="left:108px"><div class="circle"><svg width="24" height="20" viewBox="0 0 24 20"><path d="M2 8L12 1l10 7v11H2z" fill="#fff"/><path d="M2 8l10 7 10-7" stroke="#153f66" fill="none" stroke-width="1.5"/></svg></div>EMAIL SUPPORT</div>
  <div class="help-item abs" style="left:236px"><div class="circle"><svg width="22" height="22" viewBox="0 0 22 22"><path d="M3 19L15 7M14 3a4 4 0 0 0 5 5" stroke="#fff" stroke-width="2.6" fill="none" stroke-linecap="round"/><path d="M4 3l15 16" stroke="#fff" stroke-width="2.2" stroke-linecap="round"/></svg></div>24/7 SUPPORT</div>
  <div class="help-item abs" style="left:364px"><div class="circle"><svg width="20" height="24" viewBox="0 0 20 24"><rect x="4" y="2" width="11" height="20" rx="2" transform="rotate(-30 10 12)" stroke="#fff" stroke-width="2" fill="none"/></svg></div>FREE PHONE</div>
  <div class="help-item abs" style="left:492px"><div class="circle"><svg width="24" height="24" viewBox="0 0 24 24"><circle cx="12" cy="12" r="11" fill="#fff"/><path d="M8.5 9a3.5 3.5 0 1 1 4.5 3.3V14" stroke="#153f66" stroke-width="2.2" fill="none"/><circle cx="13" cy="18" r="1.4" fill="#153f66"/></svg></div>FAQ</div>
</section>

<section class="partners abs" aria-label="Partner brands">
  <svg class="abs" style="left:99px;top:27px" width="10" height="14" viewBox="0 0 10 14"><path d="M8 1L2 7l6 6" stroke="#c0272d" stroke-width="3" fill="none"/></svg>
  <div class="badge abs" style="left:117px;width:32px"></div>
  <div class="badge abs" style="left:184px;width:60px"></div>
  <div class="badge abs" style="left:264px;width:68px"></div>
  <div class="badge abs" style="left:365px;width:32px"></div>
  <div class="badge abs" style="left:437px;width:55px"></div>
  <div class="badge abs" style="left:525px;width:41px"></div>
  <svg class="abs" style="left:581px;top:27px" width="10" height="14" viewBox="0 0 10 14"><path d="M2 1l6 6-6 6" stroke="#c0272d" stroke-width="3" fill="none"/></svg>
</section>

<footer class="site-footer abs">
  <div class="foot-col abs" style="left:100px"><h3>COPYRIGHT</h3><div class="small">© 2014 Privacy policy</div></div>
  <div class="foot-col abs" style="left:228px"><h3>Important Links</h3><ul><li>Affiliate Program</li><li>Special Promotions</li><li>Newsletter</li><li>Contact</li></ul></div>
  <div class="foot-col abs" style="left:356px"><h3>Support Menu</h3><ul><li>Lost Password?</li><li>Forgot your Username?</li><li>Your Membership</li><li>Your Account</li><li>Support Forum</li></ul></div>
  <div class="foot-col abs" style="left:483px"><h3>About Us</h3><ul><li>Customer focus</li><li>Performance</li><li>Innovation</li><li>Responsibility</li></ul></div>
</footer>
<a class="foot-brand abs" href="#"><span class="brand-dot"></span><span class="brand-name">Loom Haven</span></a>
<span class="social abs" style="left:100px"></span>
<span class="social abs" style="left:119px"></span>
<span class="social abs" style="left:138px"></span>
<span class="social abs" style="left:156px"></span>

</body>
</html>
```